Tallowreed Consulting Schedule Of Rates

We need a brochure / proposal for our new company. Our company is a start up based in Australia who provides engineering and sales support to other renewable energy companies. Our brochure is a pitch-deck / sales item that catalogues our key services. We are engineering consultants.

Our website is www.tallowreedpartners.com.au. Please review the website to get a feel of colour schemes etc.

We are looking for a strong, trustworthy feel, but the brochure also needs to be sales driven and to the point.

The second page that contains the $30 price point needs to be loud and clear.

The use of relevant icons throughout the document will be viewed favorably.

Please format the tables to look attractive.

The document will need to be in an editable format so content can be edited by us at a later date.

Please feel free to use the pics within the attached word document. The winning design will be provided with updated, clearer images upon request.

Thank you

Target Market(s)

Businesses that either sell or install solar PV and other renewable energy systems in Australia. Most of target market are likely to be electrical contractors.

Industry/Entity Type

Engineering

Colors
0255a3
0492cd
ffffff

Requirements
Must have
• Icons, graphics presentation, Clean and Clear, Business oriented. Sharp sales feel
Nice to have
• solar picture backgrounds maybe
Should not have
• cartoons, over sales driven,

```html
<!DOCTYPE html>
<html lang="en">
<head>
<meta charset="utf-8">
<title>Tallowreed Consulting – Schedule Of Rates</title>
<link rel="stylesheet" href="https://fonts.googleapis.com/css2?family=Raleway:wght@300;400;700&family=Roboto+Condensed:wght@700&family=Open+Sans:wght@400&display=swap">
<style>
  :root {
    --stage: #e9e7e3;
    --paper: #ffffff;
    --navy: #1d2b3e;
    --teal: #5cc3c1;
    --gold: #e6b722;
    --sky-top: #4f86cc;
    --sky-bottom: #a8c8e8;
    --panel: #26386a;
    --ink: #1f2a38;
    --muted: #8a8f96;
  }
  * { box-sizing: border-box; margin: 0; padding: 0; }
  html, body { width: 1200px; height: 804px; overflow: hidden; background: var(--stage); }
  .canvas { position: relative; width: 1200px; height: 804px; display: flex; align-items: center; justify-content: center; }
  .cover {
    position: relative; width: 552px; height: 780px; background: var(--paper);
    box-shadow: 0 6px 22px rgba(0,0,0,.18); overflow: hidden;
  }
  .brand { position: absolute; left: 42px; top: 44px; color: var(--navy); font-family: "Raleway", sans-serif; font-weight: 700; }
  .brand-name { font-size: 30px; letter-spacing: -0.5px; line-height: 1; }
  .brand-sub { font-size: 9px; letter-spacing: 3.4px; margin-top: 4px; text-transform: uppercase; }
  .cover-art { position: absolute; left: 0; top: 118px; width: 552px; height: 500px; }
  .title-main {
    position: absolute; left: 54px; top: 530px; color: #fff;
    font-family: "Raleway", sans-serif; font-weight: 400; font-size: 27px; letter-spacing: 1px; text-transform: uppercase;
  }
  .title-sub {
    position: absolute; left: 54px; top: 580px; color: #fff;
    font-family: "Raleway", sans-serif; font-weight: 300; font-size: 21px;
  }
  .range {
    position: absolute; left: 54px; top: 642px; color: var(--ink);
    font-family: "Roboto Condensed", sans-serif; font-weight: 700; font-size: 22px;
  }
  .contact { position: absolute; left: 54px; right: 30px; top: 728px; display: flex; justify-content: space-between; }
  .contact-item {
    display: flex; align-items: center; gap: 7px;
    font-family: "Open Sans", sans-serif; font-size: 8.5px; color: var(--muted);
  }
  .contact-item::before { content: ""; width: 9px; height: 9px; background: var(--gold); flex: none; }
</style>
</head>
<body>
<div class="canvas">
  <section class="cover">
    <header class="brand">
      <div class="brand-name">Tallowreed</div>
      <div class="brand-sub">Consulting Group</div>
    </header>

    <svg class="cover-art" viewBox="0 0 552 500" xmlns="http://www.w3.org/2000/svg">
      <defs>
        <linearGradient id="skyFill" x1="0" y1="0" x2="0" y2="1">
          <stop offset="0" stop-color="var(--sky-top)"/>
          <stop offset="0.65" stop-color="var(--sky-bottom)"/>
          <stop offset="1" stop-color="var(--panel)"/>
        </linearGradient>
      </defs>
      <rect class="hero-photo" role="img" aria-label="Photo: two engineers in hard hats and hi-vis vests reviewing a laptop beside rooftop solar panels under a blue sky" x="0" y="0" width="552" height="420" fill="url(#skyFill)"/>
      <polygon class="accent-line" points="0,402 552,372 552,378 0,408" fill="var(--gold)"/>
      <polygon class="band-title" points="0,408 552,378 552,440 0,456" fill="var(--navy)"/>
      <polygon class="band-sub" points="0,456 552,440 552,470 0,496" fill="var(--teal)"/>
    </svg>

    <h1 class="title-main">Design &amp; Support Services</h1>
    <h2 class="title-sub">Schedule Of Rates</h2>
    <p class="range">Grid and Off Grid 5kW – 10MW</p>

    <footer class="contact">
      <span class="contact-item">12 Wattle Grove Rd Ringwood, 3134 Australia</span>
      <span class="contact-item">www.tallowreedpartners.com.au</span>
      <span class="contact-item">info@tallowreedpartners.com.au</span>
    </footer>
  </section>
</div>
</body>
</html>
```